College Apartment Leasing Flyer

We need a post card/flyer design for a college apartment rental company called RV Stewardship Partners. We lease apartments to college students and would like a post card/flyer that appeal to college students, that are bright colors and eye catching. We would like pictures showcasing our properties with various amenities including big kitchens, living rooms with 50 inch flat screen TVs, large outdoor patios, large rooftop decks, private bathrooms, and much more. Granite countertops, hardwood floors, ceiling fans are some of the many amenities these apartments offer college students.

We want a flyer that advertises these apartments based on the pictures attached, and advertising that we are beginning to kick off our new leasing season. These apartments are ready to be rented, and we are looking to advertise these apartments to Harrowfield College college students looking for apartments.
Updates

Project Deadline Extended
Reason: I would like to see fun design elements incorporated into the flyer. Big, bold print and pictures are the main attraction

Target Market(s)

College students

Industry/Entity Type

Real Estate

Font styles to use
Sans Serif

Colors
abd037
6b449b

Requirements
Must have
• Bright colors, big bold print, pictures of college apartments
Nice to have
• I would like to see multiple pictures with BIG print
Should not have
• Animated pictures

```html
<!DOCTYPE html>
<html lang="en">
<head>
<meta charset="utf-8">
<title>RV Stewardship Partners – Leasing Flyer</title>
<link href="https://fonts.googleapis.com/css2?family=Cinzel:wght@700&family=Open+Sans:wght@400;600;700&display=swap" rel="stylesheet">
<style>
  :root {
    --green: #abd037;
    --purple: #6b449b;
    --ink: #3c3c3c;
    --grey: #6d6d6d;
    --paper: #ffffff;
    --rule: #d9d9d9;
  }
  * { margin: 0; padding: 0; box-sizing: border-box; }
  html, body { width: 900px; height: 1200px; overflow: hidden; background: var(--paper); }
  body { font-family: "Open Sans", Arial, sans-serif; color: var(--ink); position: relative; }

  .header { position: absolute; left: 40px; right: 40px; top: 44px; height: 170px; display: flex; justify-content: space-between; }
  .brand { display: flex; align-items: center; gap: 16px; margin-top: 70px; align-self: flex-start; }
  .brand-square { width: 46px; height: 46px; background: var(--purple); }
  .brand-name { font-size: 30px; font-weight: 400; color: var(--grey); }
  .contact { font-style: normal; font-size: 23px; line-height: 1.3; color: var(--ink); margin-right: 20px; margin-top: 10px; }

  .gallery { position: absolute; left: 40px; top: 236px; width: 820px; height: 510px; display: grid;
    grid-template-columns: 201px 201px 402px; grid-template-rows: repeat(3, 1fr); gap: 8px; }
  .photo { width: 100%; height: 100%; }
  .photo-feature { grid-column: 3; grid-row: 1 / span 3; background: linear-gradient(160deg, #d9d4cc 0%, #8a3a2a 40%, #5e2318 70%, #9c948a 100%); }
  .photo-stairs { background: linear-gradient(135deg, #efece8 0%, #a8442e 55%, #d8d2ca 100%); }
  .photo-roof { background: linear-gradient(180deg, #7fa9d4 0%, #c8d8e6 50%, #8d8b86 100%); }
  .photo-living { background: linear-gradient(135deg, #e6e0d6 0%, #8a5a3c 60%, #5a4a3e 100%); }
  .tile { background: var(--green); color: #fff; display: flex; flex-direction: column; align-items: center; justify-content: center; text-align: center; }
  .tile-num { font-size: 60px; font-weight: 700; line-height: 1; }
  .tile-label { font-size: 25px; font-weight: 700; text-transform: uppercase; line-height: 1.1; margin-top: 6px; }

  .title-band { position: absolute; left: 40px; top: 760px; width: 820px; height: 60px; background: var(--purple);
    display: flex; align-items: center; justify-content: center; }
  .title-band h1 { font-family: "Cinzel", Georgia, serif; color: #fff; font-size: 37px; letter-spacing: 1px; }

  .details { position: absolute; left: 40px; top: 830px; width: 820px; height: 298px; display: flex; gap: 30px; }
  .details h2 { font-size: 22px; color: var(--purple); font-weight: 700; border-bottom: 2px solid var(--rule); padding-bottom: 2px; margin-bottom: 10px; }
  .description { width: 360px; font-size: 13px; line-height: 1.36; }
  .description .cta { margin-top: 12px; font-weight: 700; text-transform: uppercase; line-height: 1.4; }
  .description .cta strong { color: var(--purple); font-size: 17px; }
  .amenities { flex: 1; }
  .amenity-cols { display: grid; grid-template-columns: 1fr 1fr; column-gap: 18px; }
  .amenity-cols ul { list-style: none; }
  .amenity-cols li { font-size: 13px; font-weight: 600; line-height: 1.3; margin-bottom: 6px; padding-left: 20px; position: relative; }
  .amenity-cols li::before { content: ""; position: absolute; left: 0; top: 4px; width: 10px; height: 10px; background: var(--green); }

  .footer-bar { position: absolute; left: 40px; top: 1138px; width: 820px; height: 36px; background: var(--purple);
    color: #fff; font-size: 19px; display: flex; align-items: center; justify-content: center; letter-spacing: 0.5px; }
</style>
</head>
<body>
  <header class="header">
    <div class="brand">
      <span class="brand-square"></span>
      <span class="brand-name">RV Stewardship Partners</span>
    </div>
    <address class="contact">
      2740 W. Linden Ave<br>
      Brookvale, PA 19380<br>
      555-014-2290<br>
      leasing@rvstewardship.com
    </address>
  </header>

  <section class="gallery">
    <div class="photo photo-stairs" role="img" aria-label="Photo of apartment staircase with wood treads"></div>
    <div class="tile"><span class="tile-num">1</span><span class="tile-label">Kitchen</span></div>
    <div class="photo photo-feature" role="img" aria-label="Photo of kitchen with cherry cabinets, granite counters and stainless appliances"></div>
    <div class="tile"><span class="tile-num">2</span><span class="tile-label">Roof</span></div>
    <div class="photo photo-roof" role="img" aria-label="Photo of rooftop deck under blue sky"></div>
    <div class="photo photo-living" role="img" aria-label="Photo of living room with hardwood floors"></div>
    <div class="tile"><span class="tile-num">3</span><span class="tile-label">Living<br>Room</span></div>
  </section>

  <div class="title-band"><h1>RV STEWARDSHIP PARTNERS</h1></div>

  <section class="details">
    <div class="description">
      <h2>DESCRIPTION</h2>
      <p>NEW Construction blocks from Harrowfield College! Beautiful 4BR/3.5BA unit on Alder St. with upgraded amenities including GRANITE COUNTER TOPS, NEW APPLIANCES, SPACIOUS BEDROOMS AND CLOSETS, HARDWOOD FLOORS, SECURITY SYSTEM, OUTDOOR PATIO, SECURITY CAMERAS, SURROUND SOUND IN LIVING ROOM AND PATIO, CEILING FANS, WASHER AND DRYER, AND MORE!</p>
      <p class="cta">We have many units to choose from.<br>Contact us today <strong>555-014-2290</strong></p>
    </div>
    <div class="amenities">
      <h2>AMENITIES</h2>
      <div class="amenity-cols">
        <ul>
          <li>4 Bedrooms</li>
          <li>3.5 Bathrooms</li>
          <li>Touch Screen Security System</li>
          <li>Outdoor Patio</li>
          <li>Security Cameras</li>
          <li>Surround sound in Living Room and Outdoor Patio</li>
          <li>Spacious Bedrooms &amp; Closets</li>
        </ul>
        <ul>
          <li>High Ceilings</li>
          <li>Granite Counter Tops</li>
          <li>Hardwood Floors</li>
          <li>In Unit Washer/Dryer</li>
          <li>Central Air/Heat</li>
          <li>New Appliances</li>
        </ul>
      </div>
    </div>
  </section>

  <div class="footer-bar">www.rvstewardship.com</div>
</body>
</html>
```